Progressive business consultancy seeking innovative and clever powerpoint design

Were looking for a PowerPoint design for our Melbourne based business consulting company, Vomin-a.

About Us:
Based in Melbourne, Australia, Vomin-a is a management consulting organisation that partners with their clients to lead the execution of strategic process and system improvement initiatives.

Vomin-a offers business advisory services in Project Management, Business Process Management, Change Management, Business Analysis and Business Intelligence. Vomin-a combines hands on delivery with coaching in best practice methodologies and approaches to build our clients capabilities ensuring their ongoing success in project implementations.

Vomin-a has extensive experience across a wide range of industries. We specialise in assisting organisations across the accounting, legal, financial services and health sectors.

Our core purpose is to help businesses in the middle market navigate transformational change through clear and focused execution and enablement.

www.vomin-a.com.au
@vomin_a

What we're looking for:
A PowerPoint template consisting of:
- a front/cover page with hero image (attached)
- a contents page
- a divider page (for different segments of the slide deck)
- a standard PowerPoint content page
- a blank PowerPoint page. (still Vomin-a themed)

The Vomin-a colours are white and blue (RGB:0/86/162 and
CMYK 97/73/4/0)

All slides should have the Vomin-a logo (attached) and a professional, almost corporate, (but not boring) theme that is consistent across all slides. The design should reflect our focus on the "e" in vomin-a, which is what we're really about - "e"xecution and "e"nablement of change.

I've attached a PNG file of our word template which shows the focus on the "e" as a watermark on the document as well as the font files if required.

Let me know if you need any further information or design specifics.

Thanks,

Lucinda
(on behalf of Gerald)

Reason: Hi Designers, We have received some really great designs. Thanks for taking the time to make your submissions. We have decided to extend the deadline as we need some more time to review and consult other colleagues on the great submissions we have received. We are also hoping we might get some additional submissions over the weekend. We would also like enough time to provide feedback on all the submissions received. Thanks for helping us out with some really creative work. Gerald @vomin_a

Reason: Hi designers, thanks for taking the time to submit your designs. We have some really great submissions. We are going to have to extend our deadline again as we just haven't had the chance to review and provide feedback on all the designs. We will be closing this project off on Tuesday March 17. Thanks Gerald @vomin_a

Target Market(s)

C-Level executives (CEO,COO,CIO) at professional services firms (Accounting and Legal), not for profit organisations and financial services firms.

Industry/Entity Type

Management Consulting

Font styles to use
Serif
Other font styles liked:
• Calibri or attached fonts

Requirements
Must have
• A PowerPoint template consisting of:
• 1) a front/cover page with hero image (attached)
• 2) a contents page
• 3) a divider page (for different segments of the slide deck)
• 4) a standard PowerPoint content page
• 5) a blank PowerPoint page. (still Vomin-a themed)
• 6) Two content
• 7) Comparison
• 8) Table
• 9) Picture column
• 10) Chevron
• The Vomin-a colours are white and blue (RGB:0/86/162 and
• CMYK 97/73/4/0)

```html
<!DOCTYPE html>
<html lang="en">
<head>
<meta charset="utf-8">
<title>Vomin-a Presentation Template</title>
<link rel="stylesheet" href="https://fonts.googleapis.com/css2?family=Mulish:wght@400;600;700;800&display=swap">
<style>
:root{
  --blue:#0056a2;
  --blue-soft:#2a6fb3;
  --ink:#333333;
  --dark:#2b2b2b;
  --dark-2:#3d3d3d;
  --frame:#000000;
  --light:#f7f7f7;
  --light-2:#dcdcdc;
  --grey:#a9a9a9;
  --grey-row:#cfcfcf;
  --white:#ffffff;
}
*{box-sizing:border-box;margin:0;padding:0}
html,body{width:1061px;height:1200px;overflow:hidden;background:var(--frame)}
body{font-family:"Mulish",Arial,sans-serif;color:var(--ink);position:relative}
.slide{position:absolute;width:518px;height:389px;overflow:hidden;background:linear-gradient(180deg,var(--white) 0%,var(--light) 55%,var(--light-2) 100%)}
.s1{left:8px;top:8px}.s2{left:535px;top:8px}
.s3{left:8px;top:406px}.s4{left:535px;top:406px}
.s5{left:8px;top:803px}.s6{left:535px;top:803px}
.top-band{position:absolute;left:0;top:0;width:100%;height:10px;background:var(--blue)}
.footer{position:absolute;left:0;bottom:0;width:100%;height:37px;background:var(--dark);border-top:4px solid var(--blue)}
.brand{position:absolute;left:20px;top:5px;color:var(--white);font-weight:600;font-size:20px;line-height:24px;display:flex;align-items:center;gap:5px}
.brand .dot{width:8px;height:8px;border-radius:50%;background:var(--white)}
.nav{position:absolute;right:14px;top:7px;display:flex;align-items:center;gap:5px}
.nav .btn{width:20px;height:18px;background:var(--blue);display:flex;align-items:center;justify-content:center}
.nav .sep{width:1px;height:18px;background:#8a8a8a;margin:0 8px}
.nav .num{color:var(--white);font-size:12px}
.heading{position:absolute;left:22px;top:15px;font-size:29px;line-height:34px;font-weight:700;color:var(--ink)}
.heading b{color:var(--blue);font-weight:700}

/* cover and closing */
.dark{background:radial-gradient(ellipse at 35% 10%,#4a4a4a 0%,var(--dark) 60%,#232323 100%)}
.dark .band{position:absolute;left:0;top:291px;width:100%;height:49px;background:var(--blue)}
.dark .footer{height:49px;border-top:none}
.dark .brand{left:28px;top:12px;font-size:23px}
.byline{position:absolute;right:30px;top:8px;text-align:right;color:var(--white);font-size:13px;line-height:17px}
.byline b{color:var(--blue-soft);font-weight:700;display:block}
.cover-title{position:absolute;left:45px;top:50px;font-weight:800;font-size:54px;line-height:53px;letter-spacing:-.5px}
.cover-title .t1{color:var(--blue)}
.cover-title .t2{color:var(--white)}
.cover-sub{position:absolute;left:45px;top:155px;color:var(--white);font-size:23px;line-height:28px}
.cover-sub span{color:var(--blue)}
.cover-body{position:absolute;left:45px;top:196px;width:340px;color:var(--white);font-size:12.5px;line-height:16px}
.chevron{position:absolute;left:418px;top:64px}
.thanks{position:absolute;right:34px;top:52px;text-align:right;font-weight:800;font-size:76px;line-height:66px;letter-spacing:-1px}
.thanks .a{color:var(--blue)}.thanks .b{color:var(--white)}

/* about */
.about{position:absolute;left:22px;top:68px;width:474px;font-size:13.6px;line-height:19px;text-align:justify;color:var(--ink)}
.about p{margin-bottom:12px}
.about b{color:var(--blue);font-weight:700}

/* services */
.services{position:absolute;left:40px;top:68px;list-style:none}
.services li{font-size:18px;font-weight:600;line-height:24.8px;position:relative;padding-left:22px}
.services li::before{content:"";position:absolute;left:2px;top:9px;width:7px;height:7px;background:var(--blue);transform:rotate(45deg)}
.team-photo{position:absolute;left:232px;top:82px;width:256px;height:224px;background:linear-gradient(180deg,rgba(60,60,70,.06),rgba(40,40,50,.28));border-radius:3px}

/* table */
.grid{position:absolute;left:25px;top:73px;width:469px;border-collapse:collapse;font-size:9.5px}
.grid th{height:24px;font-size:13px;font-weight:800;text-align:center}
.grid th.cat{background:var(--grey);color:var(--ink)}
.grid th.o1{background:var(--blue);color:var(--white);width:112px}
.grid th.o2{background:var(--dark-2);color:var(--white);width:117px}
.grid td{height:18px}
.grid tr.group td{background:var(--grey-row);font-weight:700;padding-left:4px;font-size:10px}
.grid td.item{padding-left:30px;background:var(--white)}
.grid tr.alt td.item{background:#ececec}
.grid td.yes{background:var(--blue);color:var(--white);text-align:center;font-size:11px}
.grid tr.alt td.yes{background:var(--blue-soft)}
.grid td.no{background:var(--dark-2);color:var(--white);text-align:center}
.grid tr.alt td.no{background:#5a5a5a}

/* contact */
.map{position:absolute;left:32px;top:73px;width:222px;height:222px;border:5px solid var(--white);box-shadow:0 0 3px rgba(0,0,0,.3);background:linear-gradient(135deg,#d9e2b8 0%,#c9d8a6 45%,#a9c7de 70%,#8fb6d6 100%)}
.contact{position:absolute;left:267px;top:74px;width:236px;font-size:9.4px;line-height:11.3px;color:var(--ink)}
.contact .lead{text-align:justify;margin-bottom:8px}
.contact b{color:var(--blue);font-weight:700}
.contact h4{color:var(--blue);font-size:11.5px;line-height:14px;font-weight:700;margin-top:7px}
.social{position:absolute;left:32px;top:313px;display:flex;align-items:center;gap:9px;font-size:12px;font-weight:700}
.social .sq{width:19px;height:19px;background:var(--blue)}
.social span{color:var(--ink)}.social span b{color:var(--blue)}
</style>
</head>
<body>

<section class="slide s1 dark">
  <div class="top-band"></div>
  <div class="cover-title"><div class="t1">TITLE</div><div class="t2">PROJECT</div></div>
  <div class="cover-sub">subtext <span>presentation</span></div>
  <p class="cover-body">Lorem ipsum dolor sit amet, consectetuer adipiscing elit. Maecenas porttitor congue massa.</p>
  <svg class="chevron" width="56" height="106" viewBox="0 0 56 106"><polygon points="0,0 24,0 56,53 24,106 0,106 30,53" fill="#ffffff"/></svg>
  <div class="band"></div>
  <footer class="footer">
    <div class="brand">Vomin-a<span class="dot"></span></div>
    <div class="byline">Presentation by<b>Martin Hale</b></div>
  </footer>
</section>

<section class="slide s2">
  <div class="top-band"></div>
  <h2 class="heading"><b>About</b> Company</h2>
  <div class="about">
    <p><b>Lorem ipsum</b> dolor sit amet, consectetuer adipiscing elit. Maecenas porttitor congue massa. Fusce posuere, magna sed pulvinar ultricies, purus lectus malesuada libero, sit amet commodo magna eros quis urna.</p>
    <p><b>Nunc viverra imperdiet enim</b>. Fusce est. Vivamus a tellus. Pellentesque habitant morbi tristique senectus et netus et malesuada fames ac turpis egestas. Proin pharetra nonummy pede. Mauris et orci.</p>
    <p><b>Aenean nec lorem</b>. In porttitor. Donec laoreet nonummy augue.</p>
    <p>Suspendisse dui purus, scelerisque at, vulputate vitae, pretium mattis, nunc. Mauris eget neque at sem venenatis eleifend. Ut nonummy.</p>
    <p><b>Fusce aliquet pede non pede</b>.<br>Suspendisse dapibus lorem pellentesque magna. Integer nulla.</p>
  </div>
  <footer class="footer">
    <div class="brand">Vomin-a<span class="dot"></span></div>
    <div class="nav">
      <div class="btn"><svg width="8" height="12" viewBox="0 0 8 12"><polyline points="6,1 2,6 6,11" fill="none" stroke="#fff" stroke-width="2.4"/></svg></div>
      <div class="btn"><svg width="8" height="12" viewBox="0 0 8 12"><polyline points="2,1 6,6 2,11" fill="none" stroke="#fff" stroke-width="2.4"/></svg></div>
      <div class="sep"></div><div class="num">2</div>
    </div>
  </footer>
</section>

<section class="slide s3">
  <div class="top-band"></div>
  <h2 class="heading"><b>Our</b> Services</h2>
  <ul class="services">
    <li>Lorem ipsum</li><li>Lorem ipsum</li><li>Lorem ipsum</li><li>Lorem ipsum</li><li>Lorem ipsum</li>
    <li>Lorem ipsum</li><li>Lorem ipsum</li><li>Lorem ipsum</li><li>Lorem ipsum</li><li>Lorem ipsum</li>
  </ul>
  <div class="team-photo" role="img" aria-label="Photo of a business team in dark suits standing together"></div>
  <footer class="footer">
    <div class="brand">Vomin-a<span class="dot"></span></div>
    <div class="nav">
      <div class="btn"><svg width="8" height="12" viewBox="0 0 8 12"><polyline points="6,1 2,6 6,11" fill="none" stroke="#fff" stroke-width="2.4"/></svg></div>
      <div class="btn"><svg width="8" height="12" viewBox="0 0 8 12"><polyline points="2,1 6,6 2,11" fill="none" stroke="#fff" stroke-width="2.4"/></svg></div>
      <div class="sep"></div><div class="num">3</div>
    </div>
  </footer>
</section>

<section class="slide s4">
  <div class="top-band"></div>
  <h2 class="heading"><b>Table</b> Presentation</h2>
  <table class="grid">
    <tr><th class="cat">CATEGORY</th><th class="o1">OPTION 1</th><th class="o2">OPTION 2</th></tr>
    <tr class="group"><td colspan="3">Category 1</td></tr>
    <tr><td class="item">Lorem ipsum dolor sit amet</td><td class="yes">Yes</td><td class="no">-</td></tr>
    <tr class="alt"><td class="item">Lorem ipsum dolor sit amet</td><td class="yes">Yes</td><td class="no">-</td></tr>
    <tr><td class="item">Lorem ipsum dolor sit amet</td><td class="yes">Yes</td><td class="no">-</td></tr>
    <tr class="group"><td colspan="3">Category 2</td></tr>
    <tr><td class="item">Lorem ipsum dolor sit amet</td><td class="yes">Yes</td><td class="no">-</td></tr>
    <tr class="alt"><td class="item">Lorem ipsum dolor sit amet</td><td class="yes">Yes</td><td class="no">-</td></tr>
    <tr><td class="item">Lorem ipsum dolor sit amet</td><td class="yes">Yes</td><td class="no">-</td></tr>
    <tr class="alt"><td class="item">Lorem ipsum dolor sit amet</td><td class="yes">Yes</td><td class="no">-</td></tr>
    <tr class="group"><td colspan="3">Category 3</td></tr>
    <tr><td class="item">Lorem ipsum dolor sit amet</td><td class="yes">Yes</td><td class="no">-</td></tr>
    <tr class="alt"><td class="item">Lorem ipsum dolor sit amet</td><td class="yes">Yes</td><td class="no">-</td></tr>
  </table>
  <footer class="footer">
    <div class="brand">Vomin-a<span class="dot"></span></div>
    <div class="nav">
      <div class="btn"><svg width="8" height="12" viewBox="0 0 8 12"><polyline points="6,1 2,6 6,11" fill="none" stroke="#fff" stroke-width="2.4"/></svg></div>
      <div class="btn"><svg width="8" height="12" viewBox="0 0 8 12"><polyline points="2,1 6,6 2,11" fill="none" stroke="#fff" stroke-width="2.4"/></svg></div>
      <div class="sep"></div><div class="num">4</div>
    </div>
  </footer>
</section>

<section class="slide s5">
  <div class="top-band"></div>
  <h2 class="heading"><b>Contact</b> Info</h2>
  <div class="map" role="img" aria-label="Map of the office region"></div>
  <div class="contact">
    <p class="lead"><b>Lorem ipsum</b> dolor sit amet, consectetuer adipiscing elit. Maecenas porttitor congue massa. Fusce posuere, magna sed pulvinar ultricies, purus lectus malesuada libero, sit amet commodo magna eros quis urna.</p>
    <h4>Address</h4><p>1234 Street Address<br>New York, America<br>67890 (U.S.A)</p>
    <h4>Phone</h4><p>0123-456-789</p>
    <h4>FAX</h4><p>0123-456-789</p>
    <h4>Email</h4><p>info@yourcompany.com</p>
    <h4>Website</h4><p>www.yourcompany.com</p>
  </div>
  <div class="social">
    <div class="sq"></div><div class="sq"></div><div class="sq"></div><div class="sq"></div>
    <span>@YOUR<b>COMPANY</b></span>
  </div>
  <footer class="footer">
    <div class="brand">Vomin-a<span class="dot"></span></div>
    <div class="nav">
      <div class="btn"><svg width="8" height="12" viewBox="0 0 8 12"><polyline points="6,1 2,6 6,11" fill="none" stroke="#fff" stroke-width="2.4"/></svg></div>
      <div class="btn"><svg width="8" height="12" viewBox="0 0 8 12"><polyline points="2,1 6,6 2,11" fill="none" stroke="#fff" stroke-width="2.4"/></svg></div>
      <div class="sep"></div><div class="num">5</div>
    </div>
  </footer>
</section>

<section class="slide s6 dark">
  <div class="top-band"></div>
  <div class="thanks"><div class="a">Thank</div><div class="b">You</div></div>
  <div class="band"></div>
  <footer class="footer">
    <div class="brand">Vomin-a<span class="dot"></span></div>
    <div class="byline">Presentation by<b>Martin Hale</b></div>
  </footer>
</section>

</body>
</html>
```